Single-sided business card for restaurant bellwether with new logo made on this site

Business card options with new logo including restaurant name, address, phone number and website. This business card is single-sided only and will be presented at the hostess desk for clients to take. I would like to see options based on a cream card background, a white card background, a yellow card background and a burgundy colored background. It needs to be elegant and traditional.

Target Market(s)

local and international crowd

Industry/Entity Type

restaurant

Contact Information for Business Card

address, website and phone number

Font styles to use
Serif

Colors
EE7325
F08F49
F5BC92
FAE3D3
FDF4ED

Requirements
Must have
• new logo, address, phone number, website
Should not have
• more than three colors

```html
<!DOCTYPE html>
<html lang="es">
<head>
<meta charset="utf-8">
<title>Restaurant Bellwether – business card options</title>
<link href="https://fonts.googleapis.com/css2?family=Cinzel:wght@500;600&family=PT+Sans&display=swap" rel="stylesheet">
<style>
  :root{
    --stage:#8f8f8f;
    --cream:#fef9ec;
    --white:#ffffff;
    --burgundy:#7a1315;
    --wine:#3c1519;
    --gold:#fbb03b;
    --ink:#2e1a1c;
  }
  *{margin:0;padding:0;box-sizing:border-box}
  html,body{width:1200px;height:777px;overflow:hidden;background:var(--stage)}
  .stage{position:relative;width:1200px;height:777px}
  .card{position:absolute;width:487px;height:278px;background:var(--cream);overflow:hidden}
  .card--a{left:77px;top:73px}
  .card--b{left:627px;top:73px}
  .card--c{left:77px;top:418px}
  .card--d{left:627px;top:418px}

  .zone{position:absolute;left:0;width:100%}
  .zone--white{background:var(--white)}
  .zone--gold{background:var(--gold)}
  .zone--burgundy{background:var(--burgundy)}

  .mark{position:absolute;left:50%;transform:translateX(-50%);display:flex;flex-direction:column;align-items:center}
  .mark--framed{padding:3px}
  .mark__frame{width:100%;height:100%;border:1.5px solid var(--cream);display:flex;align-items:flex-end;justify-content:center;padding-bottom:16px}
  .mark__square{display:block}
  .mark__name{font-family:"Cinzel",serif;font-weight:600;white-space:nowrap;line-height:1}
  .mark__name--small{font-size:8px;letter-spacing:.6px;color:var(--cream)}
  .mark__name--large{font-size:12px;letter-spacing:1.6px;color:var(--wine);margin-top:6px}

  .title{position:absolute;left:0;width:100%;text-align:center;font-family:"Cinzel",serif;font-weight:600;font-size:20px;letter-spacing:.3px;line-height:1;white-space:nowrap}

  .contact{position:absolute;left:0;width:100%;font-family:"PT Sans",sans-serif;font-size:12.4px;color:var(--ink)}
  .contact .icon{position:absolute;width:14px;height:14px}
  .contact .line{position:absolute;white-space:nowrap}
  .icon path,.icon circle{fill:none;stroke-width:1.4;stroke-linecap:round;stroke-linejoin:round}
</style>
</head>
<body>
<div class="stage">

  <!-- Option A: cream with burgundy band -->
  <section class="card card--a">
    <div class="mark mark--framed" style="top:28px;width:84px;height:122px;background:var(--wine)">
      <div class="mark__frame"><span class="mark__name mark__name--small">BELLWETHER</span></div>
    </div>
    <div class="zone zone--burgundy" style="top:164px;height:33px"></div>
    <h1 class="title" style="top:171px;color:var(--cream)">RESTAURANT BELLWETHER</h1>
    <div class="contact" style="top:206px">
      <svg class="icon" style="left:46px;top:2px" viewBox="0 0 14 14"><path d="M7 13s-4.5-4.6-4.5-7.6a4.5 4.5 0 0 1 9 0C11.5 8.4 7 13 7 13z" stroke="var(--ink)"/><circle cx="7" cy="5.5" r="1.6" stroke="var(--ink)"/></svg>
      <span class="line" style="left:81px;top:0">Jacaranda 415</span>
      <span class="line" style="left:81px;top:16.5px">Bahías del Sol,</span>
      <span class="line" style="left:81px;top:33px">Oaxaca CP 70150</span>
      <svg class="icon" style="left:237px;top:1px" viewBox="0 0 14 14"><path d="M3 1.5l2 2.5-1 1.5c.8 1.8 2.2 3.2 4 4l1.5-1 2.5 2-1 2c-4.5 0-9.5-5-9.5-9.5z" stroke="var(--ink)"/><path d="M8.5 2.5a3 3 0 0 1 3 3M8.5 0.5a5 5 0 0 1 5 5" stroke="var(--ink)"/></svg>
      <svg class="icon" style="left:237px;top:20px" viewBox="0 0 14 14"><path d="M3 1l8 5.5-3.5.8 2.2 4.2-1.6.8-2.2-4.2L3 10.5z" stroke="var(--ink)"/></svg>
      <span class="line" style="left:274px;top:0">Reservaciones 958-555-0142</span>
      <span class="line" style="left:274px;top:19px">www.bellwether.com.mx</span>
    </div>
  </section>

  <!-- Option B: cream and white -->
  <section class="card card--b">
    <div class="mark" style="top:31px">
      <span class="mark__square" style="width:85px;height:60px;background:var(--wine)"></span>
      <span class="mark__name mark__name--large">BELLWETHER</span>
    </div>
    <div class="zone zone--white" style="top:189px;height:89px"></div>
    <h1 class="title" style="top:159px;color:var(--wine)">RESTAURANT BELLWETHER</h1>
    <div class="contact" style="top:200px">
      <svg class="icon" style="left:52px;top:2px" viewBox="0 0 14 14"><path d="M7 13s-4.5-4.6-4.5-7.6a4.5 4.5 0 0 1 9 0C11.5 8.4 7 13 7 13z" stroke="var(--gold)"/><circle cx="7" cy="5.5" r="1.6" stroke="var(--gold)"/></svg>
      <span class="line" style="left:80px;top:0">Jacaranda 415</span>
      <span class="line" style="left:80px;top:19.5px">Bahías del Sol,</span>
      <span class="line" style="left:80px;top:39px">Oaxaca CP 70150</span>
      <svg class="icon" style="left:245px;top:1px" viewBox="0 0 14 14"><path d="M3 1.5l2 2.5-1 1.5c.8 1.8 2.2 3.2 4 4l1.5-1 2.5 2-1 2c-4.5 0-9.5-5-9.5-9.5z" stroke="var(--gold)"/><path d="M8.5 2.5a3 3 0 0 1 3 3M8.5 0.5a5 5 0 0 1 5 5" stroke="var(--gold)"/></svg>
      <svg class="icon" style="left:245px;top:25px" viewBox="0 0 14 14"><path d="M3 1l8 5.5-3.5.8 2.2 4.2-1.6.8-2.2-4.2L3 10.5z" stroke="var(--gold)"/></svg>
      <span class="line" style="left:274px;top:0">Reservaciones 958-555-0142</span>
      <span class="line" style="left:274px;top:24px">www.bellwether.com.mx</span>
    </div>
  </section>

  <!-- Option C: cream with gold band -->
  <section class="card card--c">
    <div class="mark" style="top:31px">
      <span class="mark__square" style="width:85px;height:60px;background:var(--gold)"></span>
      <span class="mark__name mark__name--large">BELLWETHER</span>
    </div>
    <div class="zone zone--gold" style="top:156px;height:33px"></div>
    <h1 class="title" style="top:163px;color:var(--white)">RESTAURANT BELLWETHER</h1>
    <div class="contact" style="top:198px">
      <svg class="icon" style="left:49px;top:2px" viewBox="0 0 14 14"><path d="M7 13s-4.5-4.6-4.5-7.6a4.5 4.5 0 0 1 9 0C11.5 8.4 7 13 7 13z" stroke="var(--gold)"/><circle cx="7" cy="5.5" r="1.6" stroke="var(--gold)"/></svg>
      <span class="line" style="left:80px;top:0">Jacaranda 415</span>
      <span class="line" style="left:80px;top:19.5px">Bahías del Sol,</span>
      <span class="line" style="left:80px;top:39px">Oaxaca CP 70150</span>
      <svg class="icon" style="left:242px;top:1px" viewBox="0 0 14 14"><path d="M3 1.5l2 2.5-1 1.5c.8 1.8 2.2 3.2 4 4l1.5-1 2.5 2-1 2c-4.5 0-9.5-5-9.5-9.5z" stroke="var(--gold)"/><path d="M8.5 2.5a3 3 0 0 1 3 3M8.5 0.5a5 5 0 0 1 5 5" stroke="var(--gold)"/></svg>
      <svg class="icon" style="left:242px;top:25px" viewBox="0 0 14 14"><path d="M3 1l8 5.5-3.5.8 2.2 4.2-1.6.8-2.2-4.2L3 10.5z" stroke="var(--gold)"/></svg>
      <span class="line" style="left:274px;top:0">Reservaciones 958-555-0142</span>
      <span class="line" style="left:274px;top:24px">www.bellwether.com.mx</span>
    </div>
  </section>

  <!-- Option D: cream, white band, gold base -->
  <section class="card card--d">
    <div class="mark" style="top:31px">
      <span class="mark__square" style="width:87px;height:62px;background:var(--wine)"></span>
      <span class="mark__name mark__name--large">BELLWETHER</span>
    </div>
    <div class="zone zone--white" style="top:160px;height:33px"></div>
    <div class="zone zone--gold" style="top:193px;height:85px"></div>
    <h1 class="title" style="top:167px;color:var(--wine)">RESTAURANT BELLWETHER</h1>
    <div class="contact" style="top:198px">
      <svg class="icon" style="left:51px;top:2px" viewBox="0 0 14 14"><path d="M7 13s-4.5-4.6-4.5-7.6a4.5 4.5 0 0 1 9 0C11.5 8.4 7 13 7 13z" stroke="var(--ink)"/><circle cx="7" cy="5.5" r="1.6" stroke="var(--ink)"/></svg>
      <span class="line" style="left:78px;top:0">Jacaranda 415</span>
      <span class="line" style="left:78px;top:19.5px">Bahías del Sol,</span>
      <span class="line" style="left:78px;top:39px">Oaxaca CP 70150</span>
      <svg class="icon" style="left:243px;top:1px" viewBox="0 0 14 14"><path d="M3 1.5l2 2.5-1 1.5c.8 1.8 2.2 3.2 4 4l1.5-1 2.5 2-1 2c-4.5 0-9.5-5-9.5-9.5z" stroke="var(--ink)"/><path d="M8.5 2.5a3 3 0 0 1 3 3M8.5 0.5a5 5 0 0 1 5 5" stroke="var(--ink)"/></svg>
      <svg class="icon" style="left:243px;top:25px" viewBox="0 0 14 14"><path d="M3 1l8 5.5-3.5.8 2.2 4.2-1.6.8-2.2-4.2L3 10.5z" stroke="var(--ink)"/></svg>
      <span class="line" style="left:272px;top:0">Reservaciones 958-555-0142</span>
      <span class="line" style="left:272px;top:24px">www.bellwether.com.mx</span>
    </div>
  </section>

</div>
</body>
</html>
```